Innovative Educational Technology Startup needs Business Cards!

"Scholar Horizon" is an all-in-one, social profile based, online portal for Companies and Students to connect and carry out their brand ambassadorship tasks and requirements. The service allows for companies to more efficiently deploy brand ambassadorship opportunities to the millions of students actively seeking on-campus work experience.

Both educational and corporate tied into one (please keep that in mind for design purposes)
Updates

Project Deadline Extended
Reason: Need time to provide feedback to the several great designs that have been created! Thanks for the patience of one more day!

Target Market(s)

Those who get the card will more than likely be business men and working adults, but many educational instructors, professors, students, marketers, and propoective collegiate students will be the main target for these cards.

Industry/Entity Type

Business

Requirements
Must have
• Our Icon-Sized Logo (SH) must be a focus in regards to imagery.
• Color scheme must be Tiffany Blue/Black/White..(base of the card either white or black).
• www.scholarhorizonhub.com located somewhere on it, but not the main point of the card. (Logo is for that)
Should not have
• Childish or Tech-Only appeal.
• Basic font.
• Rather there be as little asymmetry in the card shape as possible. (curved edges is fine)

```html
<!DOCTYPE html>
<html lang="en">
<head>
<meta charset="utf-8">
<title>Scholar Horizon – Business Cards</title>
<link rel="stylesheet" href="https://fonts.googleapis.com/css2?family=Cinzel:wght@500&family=Questrial&display=swap">
<style>
  :root {
    --tiffany: #1de3e8;
    --tiffany-soft: rgba(255,255,255,0.22);
    --ink: #0b0b0b;
    --ink-soft: #1c1c1c;
    --paper: #ffffff;
    --backdrop: #151515;
    --graphite: #2e2e2e;
  }
  * { margin: 0; padding: 0; box-sizing: border-box; }
  html, body { width: 1200px; height: 900px; overflow: hidden; }
  body { background: var(--backdrop); position: relative; font-family: "Questrial", sans-serif; }

  .brand-name {
    font-family: "Cinzel", serif;
    font-weight: 500;
    letter-spacing: 1px;
    white-space: nowrap;
  }
  .brand-mark {
    display: block;
    width: 64px; height: 64px;
    background: var(--tiffany);
    margin: 0 auto 22px;
  }

  /* Front card – black base */
  .card-front {
    position: absolute; left: 0; top: 38px;
    width: 638px; height: 337px;
    background: linear-gradient(160deg, var(--ink-soft) 0%, var(--ink) 55%, #000 100%);
  }
  .card-front .lockup {
    position: absolute; left: 0; right: 0; top: 96px;
    text-align: center;
  }
  .card-front .brand-name { color: var(--paper); font-size: 36px; }
  .card-front .stripe {
    position: absolute; left: 0; right: 0; bottom: 30px;
    height: 10px; background: var(--tiffany);
  }

  /* Logo on dark */
  .logo-on-dark {
    position: absolute; left: 40px; top: 555px; width: 440px;
    text-align: center;
  }
  .logo-on-dark .brand-name { color: var(--paper); font-size: 40px; }

  /* Back card – white base */
  .card-back {
    position: absolute; left: 522px; top: 483px;
    width: 640px; height: 350px;
    background: var(--paper);
  }
  .card-back .lockup {
    position: absolute; left: 0; width: 448px; top: 90px;
    text-align: center;
  }
  .card-back .brand-name { color: var(--graphite); font-size: 32px; }
  .card-back .stripe {
    position: absolute; left: 0; right: 0; bottom: 12px;
    height: 10px; background: var(--tiffany);
  }
  .contact-panel {
    position: absolute; right: 0; top: 0;
    width: 192px; height: 328px;
    background: var(--tiffany);
    color: var(--paper);
    text-align: right;
    padding: 0 16px;
  }
  .contact-panel .panel-square {
    position: absolute; left: 14px; top: 14px;
    width: 160px; height: 130px;
    background: var(--tiffany-soft);
  }
  .contact-panel .person {
    position: absolute; right: 16px; top: 184px;
  }
  .person-name { font-size: 19px; font-weight: 700; letter-spacing: 0.5px; }
  .person-role { font-size: 11px; margin-top: 1px; }
  .contact-lines {
    position: absolute; right: 16px; top: 252px;
    font-size: 12px; line-height: 19px;
  }
</style>
</head>
<body>

  <section class="card-front" aria-label="Business card front">
    <div class="lockup">
      <span class="brand-mark"></span>
      <span class="brand-name">Scholar Horizon</span>
    </div>
    <div class="stripe"></div>
  </section>

  <section class="logo-on-dark" aria-label="Brand name on dark">
    <span class="brand-mark"></span>
    <span class="brand-name">Scholar Horizon</span>
  </section>

  <section class="card-back" aria-label="Business card back">
    <div class="lockup">
      <span class="brand-mark"></span>
      <span class="brand-name">Scholar Horizon</span>
    </div>
    <aside class="contact-panel">
      <span class="panel-square"></span>
      <div class="person">
        <p class="person-name">Marcus Ellery</p>
        <p class="person-role">Managing Director</p>
      </div>
      <div class="contact-lines">
        <p>P: (555) 014 22 900</p>
        <p>F: (555) 014 22 901</p>
        <p>www.scholarhorizonhub.com</p>
      </div>
    </aside>
    <div class="stripe"></div>
  </section>

</body>
</html>
```